Create look and feel for existing Web Page

Update Web Page

We have a website at http://www.usekivra.com/index-web.html. It is a single page html site, with a custom signup form. We also have a quill bay plugin at the bottom of the page. We'd like to redesign the look and feel of the entire site. We sell software to eye doctors. Also called optometrists, our software tool makes it easy for doctors to manage patients, bill, and document patient encounters. I have included our logos below.

We are looking for a new design preferably in HTML 5, CSS etc. The fields on the form on this page: http://www.usekivra.com/index-web.html

You can get screen shots of our software application at this site: http://staging.usekivra.com
username: test@samplevora.com
password: password

```html
<!DOCTYPE html>
<html lang="en">
<head>
<meta charset="utf-8">
<title>Tavimo — Choose How You Spend Your Time</title>
<link href="https://fonts.googleapis.com/css2?family=Poppins:wght@300;400;500;600;700&display=swap" rel="stylesheet">
<style>
:root{
  --orange:#f47321;
  --orange-soft:#fde3d1;
  --peach:#fdf0e7;
  --peach-deep:#fae2d1;
  --ink:#2f2f33;
  --text:#55555b;
  --muted:#8a8a90;
  --page:#f7f7f8;
  --white:#ffffff;
  --field:#ececee;
  --dark-btn:#2b2f36;
}
*{box-sizing:border-box;margin:0;padding:0}
html,body{width:1200px;height:2983px;overflow:hidden}
body{font-family:"Poppins",sans-serif;color:var(--ink);background:var(--page);position:relative}
.abs{position:absolute}
a{text-decoration:none;color:inherit}

.hero-bg{left:0;top:0;width:1200px;height:560px;
  background:radial-gradient(ellipse 720px 520px at 1050px 120px,var(--peach-deep) 0%,rgba(250,226,209,.5) 45%,rgba(247,247,248,0) 75%)}
.pricing-bg{left:0;top:1470px;width:1200px;height:630px;
  background:linear-gradient(180deg,rgba(253,240,231,0) 0%,var(--peach) 18%,var(--peach) 100%)}

/* nav */
.brand{font-weight:400;color:#6b6b70;letter-spacing:1px}
.nav-logo{left:90px;top:20px;font-size:46px;line-height:60px}
.nav{right:90px;top:32px;display:flex;align-items:center;gap:28px;font-size:15px;font-weight:500;color:#6b6b70}
.nav .active{color:var(--orange)}
.btn{display:inline-flex;align-items:center;justify-content:center;border-radius:30px;font-weight:500;white-space:nowrap}
.btn-orange{background:var(--orange);color:var(--white)}
.nav .btn{width:97px;height:34px;font-size:15px;margin-left:8px}

/* hero */
.eyebrow{color:var(--orange);font-weight:400}
.hero-eyebrow{left:89px;top:174px;font-size:22px}
.hero-title{left:89px;top:203px;font-size:49px;line-height:51px;font-weight:700;color:var(--ink)}
.hero-text{left:89px;top:327px;width:505px;font-size:14px;line-height:21px;color:var(--text)}
.hero-btn{left:89px;top:409px;width:237px;height:43px;font-size:15px}
.device{left:611px;top:141px;width:500px;height:330px;border-radius:10px;
  background:linear-gradient(90deg,#3a3a3e 0 17%,#8d8d91 17% 100%);box-shadow:0 10px 30px rgba(0,0,0,.12);border:14px solid #fff}
.device-base{left:564px;top:467px;width:592px;height:12px;border-radius:0 0 12px 12px;background:linear-gradient(#e9e9ec,#cfcfd4)}

/* features */
.center{left:0;width:1200px;text-align:center}
.feat-eyebrow{top:590px;font-size:21px}
.feat-title{top:615px;font-size:38px;line-height:45px;font-weight:600}
.feat-text{top:720px;font-size:14.5px;line-height:21px;color:var(--text)}
.card{width:293px;height:324px;background:var(--white);border-radius:150px 150px 40px 150px;
  box-shadow:0 6px 24px rgba(0,0,0,.04);text-align:center;padding:70px 40px 0}
.card.tint{background:var(--peach-deep)}
.icon{width:88px;height:86px;margin:0 auto;border-radius:16px}
.card h3{font-size:27px;font-weight:500;margin-top:22px;line-height:34px}
.card p{font-size:14px;line-height:19px;color:var(--text);margin-top:10px}

/* pricing */
.price-eyebrow{top:1556px;font-size:22px;font-weight:500}
.price-title{top:1580px;font-size:40px;font-weight:600}
.plan{background:var(--white);text-align:center;box-shadow:0 4px 20px rgba(0,0,0,.04)}
.plan .icon{border-radius:12px}
.plan h3{font-weight:500;color:var(--ink)}
.plan .amount{color:var(--ink)}
.plan .amount b{font-weight:400}
.plan .per{color:var(--orange)}
.plan p{color:var(--text)}
.plan-side{width:286px;height:294px;padding:34px 30px 0}
.plan-side .icon{width:56px;height:58px}
.plan-side h3{font-size:22px;margin-top:16px}
.plan-side .amount{font-size:16px;line-height:28px}
.plan-side .amount b{font-size:29px}
.plan-side .per{font-size:12px}
.plan-side p{font-size:12px;line-height:17px;margin-top:6px}
.plan-side .choose{margin-top:12px;width:98px;height:28px;font-size:12px;background:var(--peach);color:var(--orange)}
.plan-main{width:339px;height:349px;padding:34px 40px 0}
.plan-main .icon{width:86px;height:86px}
.plan-main h3{font-size:25px;margin-top:16px}
.plan-main .amount{font-size:18px;line-height:34px}
.plan-main .amount b{font-size:35px}
.plan-main .per{font-size:14px}
.plan-main p{font-size:14.5px;line-height:21px;margin-top:8px}
.plan-main .choose{margin-top:12px;width:116px;height:34px;font-size:14px}

/* waitlist */
.wait-eyebrow{left:84px;top:2249px;font-size:22px}
.wait-title{left:84px;top:2276px;font-size:39px;line-height:40px;font-weight:600}
.wait-text{left:84px;top:2371px;width:480px;font-size:14.5px;line-height:21px;color:var(--text)}
.field{background:var(--field);font-size:16px;color:#6b6b70;padding:0 22px;display:flex;align-items:center}
.field.area{align-items:flex-start;padding-top:18px}
.submit{left:911px;top:2447px;width:199px;height:42px;background:var(--dark-btn);color:var(--white);font-size:16px}

/* banner */
.banner{left:89px;top:2553px;width:1021px;height:142px;background:var(--orange);border-radius:8px}
.banner h2{position:absolute;left:35px;top:48px;font-size:35px;font-weight:600;color:var(--white)}
.banner .btn{position:absolute;left:755px;top:44px;width:229px;height:54px;background:var(--white);color:var(--orange);font-size:17px}

/* footer */
.foot-logo{left:139px;top:2780px;font-size:76px;line-height:90px}
.foot-col h4{font-size:18px;font-weight:500;color:var(--ink);margin-bottom:14px}
.foot-col li{list-style:none;font-size:13px;color:var(--text);line-height:22px}
.social li{display:flex;align-items:center;gap:9px;line-height:29px}
.dot{width:26px;height:26px;border-radius:50%;display:inline-block}
.foot-col .sub{font-size:12.5px;color:var(--text)}
.news{margin-top:14px;width:190px;height:40px;background:var(--white);border-radius:20px;box-shadow:0 3px 12px rgba(0,0,0,.08);
  display:flex;align-items:center;justify-content:space-between;padding:0 16px 0 18px;font-size:13px;color:var(--ink)}
.rule{left:89px;top:2938px;width:1021px;height:1px;background:#e2e2e5}
.copy{top:2952px;font-size:14px;color:var(--ink)}
</style>
</head>
<body>
<div class="abs hero-bg"></div>
<div class="abs pricing-bg"></div>

<header>
  <div class="abs brand nav-logo">tavimo</div>
  <nav class="abs nav">
    <a class="active" href="#">HOME</a>
    <a href="#">Products</a>
    <a href="#">Pricing</a>
    <a class="btn btn-orange" href="#">Sign Up</a>
  </nav>
</header>

<section>
  <p class="abs eyebrow hero-eyebrow">Lease Practices:</p>
  <h1 class="abs hero-title">Choose How You<br>Spend Your Time</h1>
  <p class="abs hero-text">Tavimo is your office operating system. Automate your painful tasks, keep track of your books, and live a litatle. Start with a FREE charting tool &amp; add more products as you grow.</p>
  <a class="abs btn btn-orange hero-btn" href="#">Get the Charting Tool for Free</a>
  <div class="abs device" role="img" aria-label="Screenshot of the Tavimo charting app showing a patient record"></div>
  <div class="abs device-base"></div>
</section>

<section>
  <p class="abs center eyebrow feat-eyebrow">Join the Cool Club</p>
  <h2 class="abs center feat-title">AI to Automate<br>Optometry Office Tasks</h2>
  <p class="abs center feat-text">Tavimo uses AI, automation, robots, &amp; other cool technology to streamline office work so you<br>can do things you love</p>

  <div class="abs card" style="left:117px;top:782px"><div class="icon" role="img" aria-label="Calendar and clock illustration" style="background:linear-gradient(135deg,#f36d5d,#f7c945)"></div><h3>Schedule</h3><p>Meet your patients where they are, 24 hours 7 days a week with the...</p></div>
  <div class="abs card" style="left:454px;top:782px"><div class="icon" role="img" aria-label="Connected laptops illustration" style="background:linear-gradient(135deg,#f7b733,#6f8fb5)"></div><h3>Intake</h3><p>Never print out another paper form. Your patients are now able to fill out...</p></div>
  <div class="abs card" style="left:793px;top:782px"><div class="icon" role="img" aria-label="Monitor with charts illustration" style="background:linear-gradient(135deg,#4bb3d6,#ef5a5a)"></div><h3>Chart</h3><p>Start charting all patient findings for FREE. With features like auto population...</p></div>

  <div class="abs card" style="left:117px;top:1135px"><div class="icon" role="img" aria-label="Invoice and coin illustration" style="background:linear-gradient(135deg,#f4a33a,#3b4d61)"></div><h3>Bill</h3><p>Don't waste your precious time or pay someone to bill insurance...</p></div>
  <div class="abs card tint" style="left:454px;top:1135px"><div class="icon" role="img" aria-label="Phone and message illustration" style="background:linear-gradient(135deg,#3b8fe0,#7fcf3d)"></div><h3>Eligible</h3><p>Don't call or login into every insurance website to get patient eligibility &amp; copays.</p></div>
  <div class="abs card" style="left:793px;top:1135px"><div class="icon" role="img" aria-label="Review form with stars illustration" style="background:linear-gradient(135deg,#f0a04b,#3f7fd0)"></div><h3>Review</h3><p>Grow your patient base &amp; improve your Searchly results with the</p></div>
</section>

<section>
  <p class="abs center eyebrow price-eyebrow">Choose</p>
  <h2 class="abs center price-title">Your Pricing</h2>

  <div class="abs plan plan-side" style="left:127px;top:1681px">
    <div class="icon" role="img" aria-label="Checklist in hand illustration" style="background:linear-gradient(135deg,#f7c945,#f5a623)"></div>
    <h3>Pick 3 Add-ons</h3>
    <div class="amount">From <b>$279</b></div>
    <div class="per">Per Locattion</div>
    <p>Choose any three features between schedule, intake, bill, eligible, and/or review.</p>
    <a class="btn choose" href="#">Choose Plan</a>
  </div>
  <div class="abs plan plan-main" style="left:431px;top:1654px">
    <div class="icon" role="img" aria-label="Calendar and clock illustration" style="background:linear-gradient(135deg,#8fc3f0,#4a90e2)"></div>
    <h3>Pick 1 Add On</h3>
    <div class="amount">From <b>$99</b></div>
    <div class="per">Per Locattion</div>
    <p>Choose between schedule, intake, bill, eligible, or review.</p>
    <a class="btn btn-orange choose" href="#">Choose Plan</a>
  </div>
  <div class="abs plan plan-side" style="left:787px;top:1681px">
    <div class="icon" role="img" aria-label="Checklist in hand illustration" style="background:linear-gradient(135deg,#f36d5d,#e8453c)"></div>
    <h3>Pick 2 Add-ons</h3>
    <div class="amount">From <b>$189</b></div>
    <div class="per">Per Locattion</div>
    <p>Choose any two features between schedule, intake, bill, eligible, &amp;/or review.</p>
    <a class="btn choose" href="#">Choose Plan</a>
  </div>
</section>

<section>
  <p class="abs eyebrow wait-eyebrow">Get on the waitlist</p>
  <h2 class="abs wait-title">Get Started With A Free<br>Charting Tool</h2>
  <p class="abs wait-text">Become part of a club that wants to change the way we practice, so we can have a life outside of the office.</p>
  <form>
    <div class="abs field" style="left:603px;top:2171px;width:247px;height:53px">Name</div>
    <div class="abs field" style="left:863px;top:2171px;width:247px;height:53px">Phone No.</div>
    <div class="abs field" style="left:603px;top:2234px;width:247px;height:53px">Email</div>
    <div class="abs field" style="left:863px;top:2234px;width:247px;height:53px">Office Name</div>
    <div class="abs field area" style="left:603px;top:2297px;width:507px;height:130px">NPI</div>
    <a class="abs btn submit" href="#">Get the free charting</a>
  </form>
</section>

<section class="abs banner">
  <h2>Now Spend Time Outside The&nbsp; Office!</h2>
  <a class="btn" href="#">Get the free charting</a>
</section>

<footer>
  <div class="abs brand foot-logo">tavimo</div>
  <div class="abs foot-col" style="left:453px;top:2762px">
    <h4>Our Links</h4>
    <ul><li>Home</li><li>Products</li><li>Pricing</li><li>Sign up</li></ul>
  </div>
  <div class="abs foot-col social" style="left:666px;top:2762px">
    <h4>Connect Links</h4>
    <ul>
      <li><span class="dot" style="background:#3b5a9a"></span>Friendline</li>
      <li><span class="dot" style="background:#2aa3ef"></span>Chirper</li>
      <li><span class="dot" style="background:#e0443a"></span>Searchly</li>
    </ul>
  </div>
  <div class="abs foot-col" style="left:867px;top:2762px">
    <h4>Our Newsletter</h4>
    <p class="sub">Subscribe To Our News Letter.</p>
    <div class="news">Enter Email
      <svg width="14" height="14" viewBox="0 0 14 14"><path d="M1 6.5 13 1 9 13 6.5 8z" fill="#f47321"/></svg>
    </div>
  </div>
  <div class="abs rule"></div>
  <p class="abs center copy">Copyright 2020 - Allright Reserved.</p>
</footer>
</body>
</html>
```